One of Australia's fastest growing Financial Company looking for an updated business card design!

Meridale Partners Australia is looking for an updated design for our business cards. We would like to keep up our professional appearances and have get new exciting design that fits our company.

The Meridale aim is to facilitate and assist clients in every financial requirement that may arise in financial areas.

We would to see the design to use colour blue and we like the clouds in the background. We have attached two designs we have use before but we need something with more professional and easy to read design.

We would like the website in the back of the card; the employees name more central and stands out; only a postal address; a list of all our locations along the bottom (Sydney, Melbourne, Brisbane, Singapore)

Looking forward to seeing the designs come in!

Target Market(s)

Other Industry Professionals
Middle Class Families

Industry/Entity Type

Finance

Contact Information for Business Card

Name; Company Role; Office Number; Mobile Number; Email Address; Website; Postal Address; Locations

Font styles to use
Serif
Sans Serif

Colors
0492cd
33a6d7
85cae6
85acd3
3176b5
0455a3
cee9f5
d5e2ee

Requirements
Must have
• Name; Company Role; Office Number; Mobile Number; Email Address; Website; Postal Address; Locations
Nice to have
• The colour blue, clouds on the background

```html
<!DOCTYPE html>
<html lang="en">
<head>
<meta charset="utf-8">
<title>Meridale Business Card</title>
<link href="https://fonts.googleapis.com/css2?family=Quicksand:wght@400;500;700&display=swap" rel="stylesheet">
<style>
  :root {
    --page: #ffffff;
    --card: #ffffff;
    --card-edge: #e2e2e2;
    --ink: #111111;
    --muted: #5f5f5f;
    --brand-blue: #1b8fd6;
    --brand-red: #e8363a;
    --faint-red: #f7d6d8;
    --sky-top: #dbe9f3;
    --sky-mid: #f4f8fb;
    --sky-low: #e6eff6;
  }
  * { box-sizing: border-box; margin: 0; padding: 0; }
  html, body {
    width: 1005px;
    height: 1200px;
    overflow: hidden;
    background: var(--page);
    font-family: "Quicksand", sans-serif;
  }
  .card {
    position: absolute;
    left: 64px;
    width: 876px;
    height: 515px;
    border: 2px solid var(--card-edge);
    background: var(--card);
    overflow: hidden;
  }
  .card--front { top: 72px; }
  .card--back { top: 611px; }

  .brand-name {
    position: absolute;
    left: 62px;
    top: 74px;
    font-size: 54px;
    font-weight: 700;
    color: var(--brand-blue);
    line-height: 1;
  }
  .identity {
    position: absolute;
    right: 38px;
    top: 36px;
    text-align: right;
    color: var(--ink);
  }
  .identity__name { font-size: 34px; font-weight: 700; line-height: 1.3; }
  .identity__role { font-size: 35px; font-weight: 500; line-height: 1.3; }

  .contact-list {
    position: absolute;
    left: 42px;
    top: 236px;
    list-style: none;
    color: var(--muted);
    font-size: 30px;
    font-weight: 500;
    line-height: 36.5px;
  }
  .watermark-name {
    position: absolute;
    right: -20px;
    top: 300px;
    font-size: 120px;
    font-weight: 700;
    color: var(--faint-red);
    opacity: 0.55;
    line-height: 1;
  }
  .website-band {
    position: absolute;
    left: 0;
    bottom: 0;
    width: 100%;
    height: 53px;
    background: var(--brand-red);
    color: #ffffff;
    font-size: 23px;
    font-weight: 500;
    letter-spacing: 0.5px;
    display: flex;
    align-items: center;
    justify-content: center;
  }

  .sky {
    position: absolute;
    inset: 0;
    background:
      radial-gradient(ellipse at 50% 45%, #ffffff 0%, rgba(255,255,255,0) 60%),
      linear-gradient(180deg, var(--sky-top) 0%, var(--sky-mid) 45%, var(--sky-low) 100%);
  }
  .lockup {
    position: absolute;
    left: 0;
    right: 0;
    top: 210px;
    display: flex;
    align-items: center;
    justify-content: center;
    gap: 22px;
  }
  .lockup__dot {
    width: 56px;
    height: 56px;
    border-radius: 50%;
    background: var(--brand-red);
  }
  .lockup__name {
    font-size: 96px;
    font-weight: 700;
    color: var(--brand-blue);
    line-height: 1;
  }
</style>
</head>
<body>
  <section class="card card--front">
    <div class="brand-name">Meridale</div>
    <div class="identity">
      <div class="identity__name">Name</div>
      <div class="identity__role">Company Role</div>
    </div>
    <ul class="contact-list">
      <li>Office Number</li>
      <li>Mobile Number</li>
      <li>Email Address</li>
      <li>Postal Address</li>
      <li>Locations</li>
    </ul>
    <div class="watermark-name" aria-hidden="true">Meridale</div>
    <div class="website-band">WWW.WEBSITE.COM</div>
  </section>

  <section class="card card--back">
    <div class="sky" role="img" aria-label="Soft pale blue sky with white clouds"></div>
    <div class="lockup">
      <span class="lockup__dot" aria-hidden="true"></span>
      <span class="lockup__name">Meridale</span>
    </div>
  </section>
</body>
</html>
```